Ridgemark Construction Letterhead

Looking for a new professional letter head for our business with one of the two logos on it. It must include all of the information listed below. The company is a heavy construction company and should have something strong looking to go along with the business. Needs to include all of the information we have listed, with nothing added. Looking for something that represents our business well. Would like it to be clean looking with nothing too fancy or colorful. Needs to be bold and strong.

Industry/Entity Type

Construction Company

Font styles to use
Sans Serif

Requirements
Must have
• One of the two logos attached
• Address - 718 Quarry Bend Rd, Niagara on the Lake, ON L0S 2K4
• Phone Number - 905-614-3871
• Fax Number - 905-614-3894
• Website - www.ridgemarkconstruction.ca
Nice to have
• Something clean and professional looking
Should not have
• Should not have the words "address", "phone number", etc.
• Only wrote those to have that info included

```html
<!DOCTYPE html>
<html lang="en">
<head>
<meta charset="utf-8">
<title>Ridgemark Construction Letterhead</title>
<link href="https://fonts.googleapis.com/css2?family=Montserrat:wght@600;700;800&display=swap" rel="stylesheet">
<style>
  :root {
    --ink: #0c0c0c;
    --paper: #ffffff;
    --gold: #98722c;
    --watermark: #efe9e1;
    --text: #1e1e1e;
    --backdrop-top: #b4b4b4;
    --backdrop-bottom: #cdebe3;
  }
  * { margin: 0; padding: 0; box-sizing: border-box; }
  html, body { width: 1200px; height: 2803px; overflow: hidden; }
  body { font-family: "Montserrat", Arial, sans-serif; position: relative; }

  .stage { position: absolute; left: 0; width: 1200px; }
  .stage--top { top: 0; height: 1400px; background: var(--backdrop-top); }
  .stage--bottom { top: 1400px; height: 1403px; background: var(--backdrop-bottom); }

  .letterhead {
    position: absolute;
    background: var(--paper);
    container-type: inline-size;
    overflow: hidden;
    box-shadow: 0 10px 30px rgba(0,0,0,0.18);
  }
  .stage--top .letterhead { left: 209px; top: 151px; width: 782px; height: 1109px; }
  .stage--bottom .letterhead { left: 158px; top: 57px; width: 843px; height: 1279px; }

  .header-band { position: absolute; left: 0; top: 0; width: 100%; height: 19.2cqw; display: block; }
  .header-band polygon { fill: var(--ink); }

  .brand {
    position: absolute; top: 3.6cqw; left: 0; width: 100%;
    display: flex; justify-content: center; align-items: center; gap: 1.6cqw;
  }
  .brand__square { width: 6.2cqw; height: 6.2cqw; background: var(--gold); }
  .brand__name {
    color: var(--paper); font-weight: 800; font-size: 3.3cqw; line-height: 1.05;
    letter-spacing: 0.02em; text-transform: uppercase;
  }

  .watermark {
    position: absolute; left: 35.6%; top: 39.6%; width: 28.8%; aspect-ratio: 1;
    background: var(--watermark); border-radius: 0.6cqw;
  }

  .contact-row {
    position: absolute; left: 0; width: 100%; bottom: 6.4%;
    font-size: 1.95cqw; font-weight: 700; color: var(--text); line-height: 1.25;
  }
  .contact { position: absolute; display: flex; align-items: center; gap: 1.6cqw; top: 0; transform: translateY(-50%); }
  .contact--address { left: 5.7cqw; }
  .contact--phone { left: 43.8cqw; }
  .contact--fax { left: 76.6cqw; }
  .contact__icon { width: 4.4cqw; height: 4.4cqw; flex: none; display: block; }
  .contact__icon circle { fill: var(--gold); }
  .contact__icon .glyph { fill: var(--paper); }

  .footer-band {
    position: absolute; left: 0; bottom: 0; width: 100%; height: 4.3cqw;
    background: var(--ink); color: var(--paper);
    display: flex; align-items: center; justify-content: center;
    font-size: 1.5cqw; font-weight: 700; letter-spacing: 0.02em;
  }
</style>
</head>
<body>

<section class="stage stage--top">
  <article class="letterhead">
    <svg class="header-band" viewBox="0 0 100 19.2" preserveAspectRatio="none" aria-hidden="true">
      <polygon points="0,0 100,0 100,10.5 50,19.2 0,10.5"/>
    </svg>
    <div class="brand">
      <span class="brand__square"></span>
      <span class="brand__name">Ridgemark<br>Construction</span>
    </div>
    <div class="watermark" aria-hidden="true"></div>
    <div class="contact-row">
      <div class="contact contact--address">
        <svg class="contact__icon" viewBox="0 0 20 20" aria-hidden="true"><circle cx="10" cy="10" r="10"/><path class="glyph" d="M10 4.2a3.6 3.6 0 0 0-3.6 3.6c0 2.7 3.6 7.3 3.6 7.3s3.6-4.6 3.6-7.3A3.6 3.6 0 0 0 10 4.2zm0 5.1a1.5 1.5 0 1 1 0-3 1.5 1.5 0 0 1 0 3z"/></svg>
        <span>718 Quarry Bend Rd, Niagara<br>on the Lake, ON L0S 2K4</span>
      </div>
      <div class="contact contact--phone">
        <svg class="contact__icon" viewBox="0 0 20 20" aria-hidden="true"><circle cx="10" cy="10" r="10"/><path class="glyph" d="M5 7.5c0-1.4 2.2-2.3 5-2.3s5 .9 5 2.3v.8h-2.6v-1h-4.8v1H5zM6.3 9h7.4l1.3 5.5H5zM10 10.3a1.6 1.6 0 1 0 0 3.2 1.6 1.6 0 0 0 0-3.2z"/></svg>
        <span>905-614-3871</span>
      </div>
      <div class="contact contact--fax">
        <svg class="contact__icon" viewBox="0 0 20 20" aria-hidden="true"><circle cx="10" cy="10" r="10"/><path class="glyph" d="M6.5 5h7v3h-7zM4.5 8.8h11v5h-2v-2h-7v2h-2zM7.2 12.4h5.6V15H7.2z"/></svg>
        <span>905-614-3894</span>
      </div>
    </div>
    <footer class="footer-band">www.ridgemarkconstruction.ca</footer>
  </article>
</section>

<section class="stage stage--bottom">
  <article class="letterhead">
    <svg class="header-band" viewBox="0 0 100 19.2" preserveAspectRatio="none" aria-hidden="true">
      <polygon points="0,0 100,0 100,10.5 50,19.2 0,10.5"/>
    </svg>
    <div class="brand">
      <span class="brand__square"></span>
      <span class="brand__name">Ridgemark<br>Construction</span>
    </div>
    <div class="watermark" aria-hidden="true"></div>
    <div class="contact-row">
      <div class="contact contact--address">
        <svg class="contact__icon" viewBox="0 0 20 20" aria-hidden="true"><circle cx="10" cy="10" r="10"/><path class="glyph" d="M10 4.2a3.6 3.6 0 0 0-3.6 3.6c0 2.7 3.6 7.3 3.6 7.3s3.6-4.6 3.6-7.3A3.6 3.6 0 0 0 10 4.2zm0 5.1a1.5 1.5 0 1 1 0-3 1.5 1.5 0 0 1 0 3z"/></svg>
        <span>718 Quarry Bend Rd, Niagara<br>on the Lake, ON L0S 2K4</span>
      </div>
      <div class="contact contact--phone">
        <svg class="contact__icon" viewBox="0 0 20 20" aria-hidden="true"><circle cx="10" cy="10" r="10"/><path class="glyph" d="M5 7.5c0-1.4 2.2-2.3 5-2.3s5 .9 5 2.3v.8h-2.6v-1h-4.8v1H5zM6.3 9h7.4l1.3 5.5H5zM10 10.3a1.6 1.6 0 1 0 0 3.2 1.6 1.6 0 0 0 0-3.2z"/></svg>
        <span>905-614-3871</span>
      </div>
      <div class="contact contact--fax">
        <svg class="contact__icon" viewBox="0 0 20 20" aria-hidden="true"><circle cx="10" cy="10" r="10"/><path class="glyph" d="M6.5 5h7v3h-7zM4.5 8.8h11v5h-2v-2h-7v2h-2zM7.2 12.4h5.6V15H7.2z"/></svg>
        <span>905-614-3894</span>
      </div>
    </div>
    <footer class="footer-band">www.ridgemarkconstruction.ca</footer>
  </article>
</section>

</body>
</html>
```